Funky new Serviced Apartment Company needs a website + logo

Bright Nest Serviced Accommodation is a new company aiming to attract customers who need temporary accommodation (2 days to 6 months) in city locations.

Our customers make considerable savings on longer stays compared to hotels, and have all the creature comforts of home including super-fast WIFI, comfy beds, full kitchen and modern, yet comfortable, furniture.

Another key feature of the design is a page to attract "Partners" who "Work with Us" by allowing us to manage their properties and becoming part of our network of accommodation units. I have include a brochure from one of our competitors, and a video can be found here: http://lnkvault-example.com/aptclip-7 - both can be used as I have permission.

The website design should work on all devices and screen sizes, and lend itself to a mobile app.

We would like to see website designs that are modern and simple, with a strong brand logo. The final design should communicate "Home From Home" and aim to attract professionals away from home on business for long periods of time.

Target Market(s)

Professional People working away from home for extended periods of time

Industry/Entity Type

Accommodation

Contact Information for Business Card

Name, Title, Phone Number, Email
Callum Fenwick, Owner, 07831 552907, callum.fenwick@brightnestsa-example.co.uk

Logo Text

Bright Nest Service Accommodation (Serviced Accommodation optional)

Coding

Coded - Design and coding required

Number of Pages Required

3 page

Font styles to use
Sans Serif

Requirements
Must have
• A 3 page website: Home, Partners, Contact Us
• Home page should have an area to list current apartment units, the user should be able to select a location and filter the list based on price and number of people.
• Partners page should inspire a "Work with us" call to action.
• The design should work with all screen sizes and devices.
• The design should say friendly and professional
Nice to have
• A simple logo, perhaps a smiling face made up using letters 'W' and 'H'.
• A neutral color scheme
Should not have
• No garish or vivid color scheme

```html
<!DOCTYPE html>
<html lang="en">
<head>
<meta charset="utf-8">
<title>Bright Nest Serviced Accommodation</title>
<link href="https://fonts.googleapis.com/css2?family=Lato:wght@400;700;900&family=Open+Sans:wght@400;600;700&display=swap" rel="stylesheet">
<style>
:root{
  --gold:#a38755;
  --gold-dark:#8c7243;
  --ink:#1f1f1f;
  --muted:#6d6d6d;
  --line:#dcdcdc;
  --paper:#ffffff;
  --mist:#ececee;
  --night:#262626;
  --head:"Lato",sans-serif;
  --body:"Open Sans",sans-serif;
}
*{box-sizing:border-box;margin:0;padding:0}
html,body{width:1200px;height:2975px;overflow:hidden;background:var(--paper)}
body{font-family:var(--body);color:var(--ink);position:relative}
section,header,footer{position:absolute;left:0;width:1200px}
.abs{position:absolute}

/* header */
.site-header{top:0;height:100px;background:var(--paper)}
.brand{left:132px;top:24px;display:flex;align-items:center;gap:14px}
.brand-mark{width:46px;height:46px;background:var(--gold)}
.brand-name{font-family:var(--head);font-weight:700;color:var(--gold);font-size:19px;line-height:23px;width:240px}
.call{right:132px;top:18px;display:flex;align-items:center;gap:8px}
.call-icon{width:26px;height:26px;border-radius:50%;background:var(--gold-dark);display:flex;align-items:center;justify-content:center}
.call-label{font-size:10px;font-weight:700;color:var(--ink)}
.call-number{font-size:21px;color:var(--gold);font-family:var(--head)}
.main-nav{right:132px;top:62px;display:flex;gap:0}
.main-nav a{font-size:11px;font-weight:600;color:var(--ink);text-decoration:none;padding:5px 12px;margin-left:12px;text-transform:uppercase}
.main-nav a.active{background:var(--gold);color:#fff}

/* hero */
.hero{top:100px;height:528px}
.hero-photo{position:absolute;inset:0;background:linear-gradient(100deg,#1c3a7a 0%,#33508c 30%,#6f7a78 55%,#8b8f86 75%,#7b6a4f 100%)}
.hero-caption{left:382px;top:190px;width:436px;height:90px;background:rgba(20,20,20,.55);text-align:center;color:#fff;padding-top:10px}
.hero-caption h1{font-family:var(--head);font-weight:900;font-size:43px;letter-spacing:.5px;line-height:48px}
.hero-caption p{font-size:15px;margin-top:2px}
.hero-dots{left:560px;top:452px;display:flex;gap:10px}
.hero-dots span{width:10px;height:10px;border-radius:50%;background:#fff}
.hero-dots span.on{background:#e23b3b}

/* section title */
.section-title{font-family:var(--head);font-weight:900;font-size:23px;color:var(--gold);text-transform:uppercase;letter-spacing:.3px}
.section-title::after{content:"";display:block;width:80px;height:3px;background:var(--gold);margin-top:12px}
.section-title.center{text-align:center}
.section-title.center::after{margin:12px auto 0;width:50px}

/* listings */
.listings{top:628px;height:510px}
.listings .section-title{left:132px;top:52px}
.filter{left:705px;top:54px}
.filter-label{font-size:10px;font-weight:700;margin-bottom:6px}
.filter-row{display:flex;gap:12px;align-items:center}
.select{width:101px;height:23px;border:1px solid #bbb;font-size:9px;padding:5px 7px;position:relative;background:#fff}
.select::after{content:"";position:absolute;right:7px;top:9px;border:4px solid transparent;border-top-color:#555}
.go{width:28px;height:23px;background:var(--gold);color:#fff;font-size:10px;font-weight:700;text-align:center;line-height:23px}
.cards{left:132px;top:132px;display:flex;gap:12px}
.card{width:228px;height:312px;border:1px solid var(--line);background:#fff;padding:4px}
.card-photo{height:210px;position:relative}
.amenities{position:absolute;left:0;right:0;bottom:0;height:20px;background:rgba(0,0,0,.75);display:flex;justify-content:space-around;align-items:center;color:#fff;font-size:8px;font-weight:700}
.card-body{padding:14px 8px 0}
.card-loc{font-size:10px;color:var(--muted);display:flex;gap:4px;align-items:center}
.card-title{font-size:12px;font-weight:700;margin-top:6px}
.card-price{font-size:17px;font-weight:700;color:var(--gold);margin-top:8px}

/* welcome */
.welcome{top:1138px;height:518px;background:var(--mist)}
.welcome .section-title{left:132px;top:62px}
.welcome-intro{left:132px;top:118px;width:390px;font-size:12px;line-height:20px;color:#333}
.features{left:150px;top:192px}
.feature{display:flex;gap:35px;align-items:center;height:44px;margin-bottom:29px}
.feature-icon{width:44px;height:44px;border-radius:50%;background:var(--gold);display:flex;align-items:center;justify-content:center}
.feature h3{font-size:12px;font-weight:700;text-transform:uppercase}
.feature p{font-size:10px;color:var(--muted);margin-top:4px}
.video{left:541px;top:119px;width:530px;height:326px;background:linear-gradient(135deg,#6c6f9a 0%,#58527e 45%,#7d6c84 100%);overflow:hidden}
.video-title{position:absolute;left:0;right:0;top:125px;text-align:center;font-family:var(--head);font-size:40px;color:rgba(255,255,255,.85);line-height:42px;letter-spacing:1px}
.play{position:absolute;left:222px;top:132px;width:78px;height:54px;border-radius:14px;background:#2a2a2a;display:flex;align-items:center;justify-content:center}

/* services */
.services{top:1656px;height:360px}
.services .section-title{left:0;width:1200px;top:58px}
.service-row{left:70px;top:168px;width:1060px;display:flex}
.service{flex:1;text-align:center;border-left:1px solid var(--line);height:96px;padding-top:8px}
.service:first-child{border-left:none}
.service p{font-size:12px;line-height:17px;margin-top:16px;color:#222}

/* testimonials */
.testimonials{top:2016px;height:389px;background:linear-gradient(180deg,#2c2c2c,#1d1d1d)}
.testimonials .section-title{left:0;width:1200px;top:58px;color:#b79a5b}
.testimonials .section-title::after{background:#b79a5b}
.quote{left:345px;top:164px;width:510px;text-align:center;font-size:12px;line-height:21px;color:#ddd}
.quote-rule{left:585px;top:282px;width:30px;height:2px;background:var(--gold)}
.quote-name{left:0;width:1200px;top:300px;text-align:center;font-size:12px;color:#ddd}
.arrow{top:186px}

/* gallery */
.gallery{top:2405px;height:235px;display:flex}
.gallery div{width:240px;height:235px}

/* footer */
.site-footer{top:2640px;height:335px;background:var(--mist)}
.foot-brand{left:132px;top:82px}
.foot-col{top:48px}
.foot-col h4{font-size:10px;font-weight:700;color:var(--gold);text-transform:uppercase;margin-bottom:18px}
.contact-item{display:flex;gap:12px;font-size:11px;line-height:17px;margin-bottom:14px}
.menu-list{list-style:none;font-size:11px;line-height:18px}
.newsletter-input{width:260px;height:38px;background:#fff;font-size:11px;padding:11px 12px;color:#333}
.signup{width:94px;height:33px;background:var(--gold);color:#fff;font-size:12px;font-weight:700;text-align:center;line-height:33px;margin-top:15px}
.foot-rule{left:132px;top:238px;width:936px;height:1px;background:#cfcfcf}
.copyright{left:0;width:1200px;top:276px;text-align:center;font-size:11px}
</style>
</head>
<body>

<header class="site-header">
  <div class="abs brand">
    <div class="brand-mark"></div>
    <div class="brand-name">Bright Nest Serviced Accommodation</div>
  </div>
  <div class="abs call">
    <div class="call-icon"><svg width="14" height="14" viewBox="0 0 24 24"><path fill="#fff" d="M6.6 10.8a15 15 0 006.6 6.6l2.2-2.2a1 1 0 011-.3 11 11 0 003.6.6 1 1 0 011 1V20a1 1 0 01-1 1A17 17 0 013 4a1 1 0 011-1h3.5a1 1 0 011 1 11 11 0 00.6 3.6 1 1 0 01-.3 1z"/></svg></div>
    <span class="call-label">CALL US :</span>
    <span class="call-number">555.014.2290</span>
  </div>
  <nav class="abs main-nav">
    <a class="active">Home</a><a>About us</a><a>Services</a><a>Apartment</a><a>Blog</a><a>Contact us</a>
  </nav>
</header>

<section class="hero">
  <div class="hero-photo" role="img" aria-label="Modern apartment buildings with balconies under a blue sky"></div>
  <div class="abs hero-caption">
    <h1>APARTMENT UNITS</h1>
    <p>There are many variations of passages of Lorem</p>
  </div>
  <div class="abs hero-dots"><span></span><span class="on"></span><span></span><span></span></div>
</section>

<section class="listings">
  <h2 class="abs section-title">List of apartments</h2>
  <div class="abs filter">
    <div class="filter-label">FILTER BY</div>
    <div class="filter-row">
      <div class="select">Location</div>
      <div class="select">Price</div>
      <div class="select">No.of People</div>
      <div class="go">GO</div>
    </div>
  </div>
  <div class="abs cards">
    <article class="card">
      <div class="card-photo" role="img" aria-label="Apartment block with timber balconies" style="background:linear-gradient(180deg,#1e5fb4 0%,#5d87c0 45%,#8b7a5a 100%)">
        <div class="amenities"><span>WIFI</span><span>BED</span><span>KITCHEN</span><span>FURNITURE</span></div>
      </div>
      <div class="card-body"><div class="card-loc"><svg width="8" height="10" viewBox="0 0 8 10"><path fill="#888" d="M4 0a4 4 0 00-4 4c0 3 4 6 4 6s4-3 4-6a4 4 0 00-4-4z"/></svg>Ashford Vale, KY</div><div class="card-title">THERE ARE MANY VARIATIONS</div><div class="card-price">$1100.00</div></div>
    </article>
    <article class="card">
      <div class="card-photo" role="img" aria-label="Red and white apartment building" style="background:linear-gradient(180deg,#6f9ad6 0%,#a4a9ad 45%,#8e3b33 100%)">
        <div class="amenities"><span>WIFI</span><span>BED</span><span>KITCHEN</span><span>FURNITURE</span></div>
      </div>
      <div class="card-body"><div class="card-loc"><svg width="8" height="10" viewBox="0 0 8 10"><path fill="#888" d="M4 0a4 4 0 00-4 4c0 3 4 6 4 6s4-3 4-6a4 4 0 00-4-4z"/></svg>Ashford Vale, KY</div><div class="card-title">THERE ARE MANY VARIATIONS</div><div class="card-price">$350.00</div></div>
    </article>
    <article class="card">
      <div class="card-photo" role="img" aria-label="Green and beige apartment building" style="background:linear-gradient(180deg,#4c82c9 0%,#8f9a7f 50%,#6a7a4e 100%)">
        <div class="amenities"><span>WIFI</span><span>BED</span><span>KITCHEN</span><span>FURNITURE</span></div>
      </div>
      <div class="card-body"><div class="card-loc"><svg width="8" height="10" viewBox="0 0 8 10"><path fill="#888" d="M4 0a4 4 0 00-4 4c0 3 4 6 4 6s4-3 4-6a4 4 0 00-4-4z"/></svg>Ashford Vale, KY</div><div class="card-title">THERE ARE MANY VARIATIONS</div><div class="card-price">$820.00</div></div>
    </article>
    <article class="card">
      <div class="card-photo" role="img" aria-label="Modern white tower block with glass balconies" style="background:linear-gradient(180deg,#3f86d8 0%,#a9bfd8 50%,#64788e 100%)">
        <div class="amenities"><span>WIFI</span><span>BED</span><span>KITCHEN</span><span>FURNITURE</span></div>
      </div>
      <div class="card-body"><div class="card-loc"><svg width="8" height="10" viewBox="0 0 8 10"><path fill="#888" d="M4 0a4 4 0 00-4 4c0 3 4 6 4 6s4-3 4-6a4 4 0 00-4-4z"/></svg>Ashford Vale, KY</div><div class="card-title">THERE ARE MANY VARIATIONS</div><div class="card-price">$910.00</div></div>
    </article>
  </div>
</section>

<section class="welcome">
  <h2 class="abs section-title">Welcome to our site</h2>
  <p class="abs welcome-intro">There are many variations of passages of Lorem Ipsum available, but the majority have suffered alteration in some</p>
  <div class="abs features">
    <div class="feature"><div class="feature-icon"><svg width="18" height="18" viewBox="0 0 24 24" fill="none" stroke="#fff" stroke-width="2"><rect x="3" y="5" width="15" height="15" rx="1"/><path d="M10 14l9-9 2 2-9 9h-2z"/></svg></div><div><h3>Regular bookings, regular payments</h3><p>Lorem Ipsum is simply dummy text of the printing</p></div></div>
    <div class="feature"><div class="feature-icon"><svg width="18" height="18" viewBox="0 0 24 24"><circle cx="12" cy="12" r="7" fill="none" stroke="#fff" stroke-width="4" stroke-dasharray="3 2.5"/><circle cx="12" cy="12" r="3" fill="#fff"/></svg></div><div><h3>Managing your bookings</h3><p>Lorem Ipsum is simply dummy text of the printing</p></div></div>
    <div class="feature"><div class="feature-icon"><svg width="18" height="18" viewBox="0 0 24 24" fill="none" stroke="#fff" stroke-width="2.4"><path d="M4 15v-3a8 8 0 0116 0v3"/><rect x="3" y="14" width="4" height="6" fill="#fff"/><rect x="17" y="14" width="4" height="6" fill="#fff"/></svg></div><div><h3>Expert support from the start</h3><p>Lorem Ipsum is simply dummy text of the printing</p></div></div>
    <div class="feature"><div class="feature-icon"><svg width="18" height="18" viewBox="0 0 24 24"><text x="12" y="19" text-anchor="middle" font-family="Open Sans,sans-serif" font-size="19" font-weight="700" fill="#fff">$</text></svg></div><div><h3>Maximise your income</h3><p>Lorem Ipsum is simply dummy text of the printing</p></div></div>
  </div>
  <div class="abs video" role="img" aria-label="Video still of a serviced bedroom with a made bed and bedside lamps">
    <div class="video-title">WELCOME TO THE<br>REVOLUTION</div>
    <div class="play"><svg width="22" height="24" viewBox="0 0 22 24"><path d="M0 0l22 12L0 24z" fill="#fff"/></svg></div>
  </div>
</section>

<section class="services">
  <h2 class="abs section-title center">Services</h2>
  <div class="abs service-row">
    <div class="service"><svg width="48" height="42" viewBox="0 0 48 42" fill="none" stroke="#a38755" stroke-width="3"><rect x="3" y="3" width="38" height="26"/><path d="M16 38h14M23 29v9"/><rect x="34" y="18" width="11" height="20" fill="#a38755"/></svg><p>Fill out our<br>enquiry form</p></div>
    <div class="service"><svg width="48" height="42" viewBox="0 0 48 42" fill="none" stroke="#a38755" stroke-width="3"><path d="M4 16l20-13 20 13v23H4z"/><path d="M4 16l20 13 20-13"/><text x="24" y="21" text-anchor="middle" font-size="12" fill="#a38755" stroke="none" font-family="Open Sans,sans-serif" font-weight="700">@</text></svg><p>Alternatively,<br>send us an email</p></div>
    <div class="service"><svg width="70" height="42" viewBox="0 0 70 42" fill="#a38755"><circle cx="15" cy="11" r="7"/><path d="M3 38c0-10 5-15 12-15s12 5 12 15z"/><circle cx="55" cy="11" r="7"/><path d="M43 38c0-10 5-15 12-15s12 5 12 15z"/><circle cx="35" cy="9" r="8"/><path d="M21 40c0-11 6-17 14-17s14 6 14 17z"/></svg><p>We have experts in<br>your area</p></div>
    <div class="service"><svg width="70" height="42" viewBox="0 0 70 42" fill="none" stroke="#a38755" stroke-width="3"><path d="M6 14h58L56 4H14z" fill="#a38755"/><rect x="10" y="14" width="50" height="25"/><path d="M16 20h8v6h-8zM46 20h8v6h-8zM30 39V24h10v15M2 40h66"/></svg><p>We'll then come and visit<br>you at your property</p></div>
    <div class="service" style="flex:1.3"><svg width="40" height="42" viewBox="0 0 40 42" fill="none" stroke="#a38755" stroke-width="3"><rect x="9" y="3" width="26" height="34"/><path d="M4 8v32h24"/><path d="M15 12h14M15 18h14M15 24h14M15 30h10"/></svg><p>Just before your property gets loaded<br>onto our systems</p></div>
  </div>
</section>

<section class="testimonials">
  <div class="abs" style="inset:0;background:linear-gradient(180deg,rgba(60,60,60,.35),rgba(20,20,20,.2))" role="img" aria-label="Dimmed night city skyline"></div>
  <h2 class="abs section-title center">Testimonials</h2>
  <svg class="abs arrow" style="left:184px" width="16" height="28" viewBox="0 0 16 28"><path d="M14 2L3 14l11 12" fill="none" stroke="#fff" stroke-width="4"/></svg>
  <svg class="abs arrow" style="left:1002px" width="16" height="28" viewBox="0 0 16 28"><path d="M2 2l11 12L2 26" fill="none" stroke="#fff" stroke-width="4"/></svg>
  <p class="abs quote">There are many variations of passages of Lorem Ipsum available, but the majority have suffered alteration in some form, by injected humour, or randomised words which don't look even slightly believable. If you are going to use a passage of Lorem Ipsum, you need to be sure there isn't anything embarrassing hidden in the middle of text.</p>
  <div class="abs quote-rule"></div>
  <p class="abs quote-name">Martin, England</p>
</section>

<section class="gallery">
  <div role="img" aria-label="Open kitchen with dark wood island" style="background:linear-gradient(180deg,#d9d4cc,#6b4a33)"></div>
  <div role="img" aria-label="Living room with lime green feature wall" style="background:linear-gradient(180deg,#e8e8e0,#9bbc3a 55%,#2e2e2e)"></div>
  <div role="img" aria-label="White lounge with fireplace" style="background:linear-gradient(180deg,#f3eee6,#c9b8a0 60%,#4a3a2c)"></div>
  <div role="img" aria-label="Bedroom with warm timber panelling" style="background:linear-gradient(180deg,#7a4c2c,#d8c6a8 60%,#a6815a)"></div>
  <div role="img" aria-label="Bright living room with white sofas" style="background:linear-gradient(180deg,#e9e6e0,#d2cbc0 60%,#8a7a69)"></div>
</section>

<footer class="site-footer">
  <div class="abs brand foot-brand" style="top:82px">
    <div class="brand-mark"></div>
    <div class="brand-name">Bright Nest Serviced Accommodation</div>
  </div>
  <div class="abs foot-col" style="left:462px">
    <h4>Contact us</h4>
    <div class="contact-item"><svg width="10" height="12" viewBox="0 0 8 10"><path fill="#a38755" d="M4 0a4 4 0 00-4 4c0 3 4 6 4 6s4-3 4-6a4 4 0 00-4-4z"/></svg><span>28 Linden Crescent<br>Harlow Bay, FL 33990</span></div>
    <div class="contact-item"><svg width="12" height="12" viewBox="0 0 24 24"><path fill="#a38755" d="M6.6 10.8a15 15 0 006.6 6.6l2.2-2.2a1 1 0 011-.3 11 11 0 003.6.6 1 1 0 011 1V20a1 1 0 01-1 1A17 17 0 013 4a1 1 0 011-1h3.5a1 1 0 011 1 11 11 0 00.6 3.6 1 1 0 01-.3 1z"/></svg><span>555.014.2290</span></div>
    <div class="contact-item" style="margin-top:20px"><svg width="12" height="10" viewBox="0 0 12 10"><rect width="12" height="10" fill="#a38755"/><path d="M0 0l6 5 6-5" fill="none" stroke="#fff"/></svg><span>hello@brightnest-example.com</span></div>
  </div>
  <div class="abs foot-col" style="left:682px">
    <h4>Menu</h4>
    <ul class="menu-list"><li>Home</li><li>About us</li><li>services</li><li>Apartments</li><li>Blog</li><li>Contact us</li></ul>
  </div>
  <div class="abs foot-col" style="left:812px">
    <h4>Newsletter</h4>
    <div class="newsletter-input">E mail id</div>
    <div class="signup">SIGNUP</div>
  </div>
  <div class="abs foot-rule"></div>
  <p class="abs copyright">Copyrights @ 2017 All Rights Reserved</p>
</footer>

</body>
</html>
```